Solvane Vitality MediSpa Brochure

We need a new brochure design. The old is attached.

We are wanting a three panel brochure for med spa designed and ready for print. The brochure will have content and images on both sides. We attached the old brochure in pdf format. The content needs to stay as on the attached pdf but please feel free to offer new designs. The color needs to match the attached logo, which is a light blue and teal. All images we want on the brochure are also attached.

The design must have an 1/8 in space from each edge for printing purposes

Target Market(s)

Men and Women

Industry/Entity Type

Wellness

Font styles to use
Sans Serif

Colors
34a6d7
33b8a4

Requirements
Must have
• soft curves. must have a 1/8 in space on all edges (including interior) to give bleed space for printing. Use content written on attached brochure.

```html
<!DOCTYPE html>
<html lang="en">
<head>
<meta charset="utf-8">
<title>Solvane Vitality MediSpa – Brochure</title>
<link href="https://fonts.googleapis.com/css2?family=Roboto+Slab:wght@300;400;500;600&display=swap" rel="stylesheet">
<style>
  :root{
    --teal:#16a3a8;
    --teal-text:#1a8e96;
    --teal-deep:#1d6b78;
    --cyan-soft:#bfe7ec;
    --cyan-mid:#8fd3dc;
    --ink:#555;
    --white:#fff;
    --gray-dark:#5f5f5f;
    --gray-light:#8a8a8a;
  }
  *{box-sizing:border-box;margin:0;padding:0}
  html,body{width:1200px;height:928px;overflow:hidden;background:#fff}
  body{font-family:"Roboto Slab",serif;color:var(--ink)}
  .brochure{position:relative;width:1200px;height:928px;overflow:hidden;background:#fff}
  .abs{position:absolute}
  .shapes{position:absolute;left:0;top:0}

  .photo{position:absolute;left:400px;top:0;width:400px;height:886px;
    background:linear-gradient(180deg,#8fd0e0 0%,#b7e2ec 30%,#d9eff4 55%,#eef7f9 75%,#f4f8f8 100%)}

  .panel-title{position:absolute;font-weight:600;font-size:27px;color:var(--white);letter-spacing:.2px;white-space:nowrap}
  .rule{position:absolute;border-top:1.5px dotted rgba(255,255,255,.85)}
  .rule.teal{border-top-color:var(--teal)}

  .tri{display:inline-block;width:12px;height:12px;background:var(--white);
    clip-path:polygon(100% 0,100% 100%,0 100%);margin-right:12px;vertical-align:-1px}
  .tri.teal{background:var(--teal-text)}

  .treatment{position:absolute;left:28px;width:350px;color:var(--white)}
  .treatment h3{font-weight:600;font-size:18px;line-height:22px;margin-left:2px}
  .treatment p{font-weight:300;font-size:14px;line-height:17.7px;margin-top:3px;white-space:nowrap}

  .inject-title{left:438px;top:52px;font-size:29px;font-weight:400;color:var(--teal-text)}
  .inject-list{position:absolute;list-style:none;font-weight:600;font-size:16px;color:var(--teal-text);line-height:25.6px}
  .inject-list li{white-space:nowrap}

  .testimonial{position:absolute;left:440px;width:330px;color:var(--white)}
  .testimonial .label{font-style:italic;font-weight:300;font-size:22px;line-height:26px}
  .testimonial .label strong{font-weight:600;font-size:24px}
  .testimonial blockquote{font-style:italic;font-weight:300;font-size:12.6px;line-height:16.8px;white-space:nowrap;margin-top:14px}
  .testimonial cite{display:block;font-style:normal;font-weight:400;font-size:14.5px;margin-top:10px}
  .testimonial cite span{font-weight:300}

  .menu{position:absolute;left:828px;list-style:none;color:var(--white);font-weight:400;font-size:17px;line-height:28.4px}
  .menu li{white-space:nowrap}
  .menu .sub{padding-left:26px;font-size:16px}
  .menu .sub b{font-weight:500}
  .menu .sub i{font-style:normal;font-weight:300;color:#dff3f4}
  .dot{display:inline-block;width:6px;height:6px;border-radius:50%;background:var(--white);margin-right:10px;vertical-align:2px}

  .skincare{left:28px;top:778px;font-weight:600;font-size:27px;line-height:34px;color:var(--teal)}

  .brand{position:absolute;left:800px;width:400px;text-align:center;color:var(--teal);font-weight:400}
  .brand .name{font-size:27px;line-height:32px}
  .brand .kind{font-size:34px;letter-spacing:9px;line-height:40px}

  .contact{position:absolute;left:800px;width:400px;text-align:center;color:var(--ink)}
  .address{top:706px;font-size:15.5px;line-height:20px}
  .phone{font-size:24px;font-weight:300;color:var(--teal);line-height:32px}
  .phone small{font-size:15px;font-weight:400}
  .email{top:850px;font-size:16.5px;letter-spacing:.3px}

  .footer{position:absolute;left:0;top:886px;width:1200px;height:42px;background:var(--teal-deep)}
  .footer .web{position:absolute;right:28px;top:9px;color:var(--white);font-size:17.5px;font-weight:400;letter-spacing:.3px}
</style>
</head>
<body>
<div class="brochure">

  <div class="photo" role="img" aria-label="Photo of a smiling woman in a white top with arms raised against a bright sky"></div>

  <svg class="shapes" width="1200" height="928" viewBox="0 0 1200 928" aria-hidden="true">
    <defs>
      <linearGradient id="quoteFill" x1="0" y1="0" x2="0" y2="1">
        <stop offset="0" stop-color="#6a6a6a"/>
        <stop offset="1" stop-color="#7d7d7d"/>
      </linearGradient>
    </defs>
    <!-- interior panel top accents -->
    <polygon points="400,0 800,0 800,140 520,40" fill="#ffffff" opacity=".18"/>
    <polygon points="400,0 640,0 800,70 800,110" fill="#ffffff" opacity=".2"/>
    <!-- left panel -->
    <polygon points="0,0 400,0 400,792 0,672" fill="var(--teal)"/>
    <polygon points="0,672 400,792 0,744" fill="var(--cyan-mid)" opacity=".75"/>
    <polygon points="0,700 400,792 0,744" fill="var(--cyan-soft)" opacity=".8"/>
    <!-- right panel -->
    <polygon points="800,0 1200,0 1200,415 800,524" fill="var(--teal)"/>
    <polygon points="880,503 1200,415 1200,470" fill="var(--cyan-mid)" opacity=".7"/>
    <polygon points="1000,490 1200,440 1200,500" fill="var(--cyan-soft)" opacity=".8"/>
    <!-- testimonial card -->
    <polygon points="418,610 778,728 778,886 418,886" fill="url(#quoteFill)"/>
  </svg>

  <!-- Left panel: laser treatments -->
  <h2 class="panel-title" style="left:28px;top:20px">Laser Treatments</h2>
  <div class="rule" style="left:28px;top:62px;width:342px"></div>

  <section class="treatment" style="top:77px">
    <h3><span class="tri"></span>Laser Hair removal</h3>
    <p>Laser hair removal is a great solution for those<br>who no longer want to continue shaving,<br>tweezing or waxing to remove unwanted hair.<br>Our innovative laser hair removal treatments<br>can permanently remove unwanted body hair.</p>
  </section>
  <section class="treatment" style="top:205px">
    <h3><span class="tri"></span>IntimaRenew</h3>
    <p>IntimaRenew is an outpatient, minimally invasive,<br>non-hormonal vaginal procedure designed to<br>stimulate new collagen productionfor healthier<br>tissue. This procedure treats dryness, itchiness,<br>loss of sensation and stress incontinence.</p>
  </section>
  <section class="treatment" style="top:334px">
    <h3><span class="tri"></span>CO2 Resurfacing</h3>
    <p>The CO2 Laser is the highest power continuous<br>laser, making it ideal for resurfacing. The<br>wavelenghts produced are ideal the energy to be<br>agsorbed in the skin and produce excellent<br>results. It reduces wrinkles, age spots, and<br>stimulates collagen production.</p>
  </section>
  <section class="treatment" style="top:480px">
    <h3><span class="tri"></span>IPL Photofacial</h3>
    <p>Brown spots, broken capillaries and other fallout<br>from photo aging are easy targets for this laser<br>system, which uses broadband light to repair<br>these defects.</p>
  </section>
  <section class="treatment" style="top:591px">
    <h3><span class="tri"></span>IPL Acne/Rosacea/Spider Vein</h3>
    <p>Acne can be treated nonablatively using IPL, a<br>relatively low-energy, short-pulse of broadband<br>light, resulting in an improvement of the skin’s<br><span style="margin-left:66px">appearance with less breakouts.</span><br><span style="margin-left:130px">Rosacea and spider veins are</span><br><span style="margin-left:196px">also reduced using</span><br><span style="margin-left:262px">IPL.</span></p>
  </section>

  <h2 class="abs skincare">Skincare &amp;<br>Dermaluxe</h2>
  <div class="rule teal" style="left:28px;top:856px;width:342px"></div>

  <!-- Middle panel: injectables -->
  <h2 class="abs inject-title">Injectables</h2>
  <div class="rule teal" style="left:438px;top:96px;width:316px"></div>
  <ul class="inject-list" style="left:440px;top:107px">
    <li><span class="tri teal"></span>Calmitox</li>
    <li><span class="tri teal"></span>Contoura</li>
    <li><span class="tri teal"></span>Easeline</li>
    <li><span class="tri teal"></span>Hyalift</li>
  </ul>
  <ul class="inject-list" style="left:628px;top:107px">
    <li><span class="tri teal"></span>Plumavel</li>
    <li><span class="tri teal"></span>PRP</li>
    <li><span class="tri teal"></span>Softela</li>
    <li><span class="tri teal"></span>Liftara</li>
    <li><span class="tri teal"></span>Formavera</li>
  </ul>

  <figure class="testimonial" style="top:674px">
    <div class="label">Client<br><strong>Testimonial</strong> <span style="display:inline-block;width:88px;border-top:1.5px dotted rgba(255,255,255,.8);vertical-align:4px"></span></div>
    <blockquote>Dr. Hale has been doing my Calmitox and Filers<br>for the past year now and I have been very<br>happy with the results. She has a caring,<br>calming touch that has helped me overcome<br>my fear of needles. I can’t say enough<br>wonderful things about Dr. Hale.</blockquote>
    <cite>Elena - <span>Happy Client</span></cite>
  </figure>

  <!-- Right panel -->
  <h2 class="panel-title" style="left:828px;top:22px">Facials &amp; Chemical Peels</h2>
  <div class="rule" style="left:828px;top:64px;width:341px"></div>
  <ul class="menu" style="top:74px">
    <li><span class="tri"></span>Micronnedling with PRP</li>
    <li><span class="tri"></span>Dermaplane Facial</li>
    <li><span class="tri"></span>Meical Grade Chemical Peel</li>
    <li><span class="tri"></span>Facials</li>
    <li><span class="tri"></span>Waxing</li>
    <li><span class="tri"></span>AquaGlow Facial</li>
  </ul>

  <h2 class="panel-title" style="left:828px;top:264px">Wellness Treatments</h2>
  <div class="rule" style="left:828px;top:307px;width:341px"></div>
  <ul class="menu" style="top:316px;line-height:27.6px">
    <li><span class="tri"></span>B-12 Injections</li>
    <li class="sub"><span class="dot"></span><b>LipoB</b> - <i>Weight Loss</i></li>
    <li class="sub"><span class="dot"></span><b>LipoB + Carnltine</b> - <i>Muscle Building</i></li>
    <li><span class="tri"></span>Hormone Replacement Therapy</li>
  </ul>

  <div class="brand" style="top:578px">
    <div class="name">Solvane Vitality</div>
    <div class="kind">MEDISPA</div>
  </div>

  <div class="contact address">482 E. Brookfield Ave<br>Suite 210, Harlow, TX 75010</div>
  <div class="rule teal" style="left:866px;top:760px;width:268px"></div>
  <div class="contact" style="top:768px">
    <div class="phone"><small>Ph: </small>(555) 214-3086</div>
    <div class="phone"><small>Fax: </small>(555) 214-3087</div>
  </div>
  <div class="rule teal" style="left:866px;top:840px;width:268px"></div>
  <div class="contact email">hello@solvanevitality.com</div>

  <footer class="footer">
    <span class="web">www.SolvaneVitalityMedispa.com</span>
  </footer>
</div>
</body>
</html>
```